New Property management company business cards

Looking for a new business card, to reflect new younger ownership
Card should be clean, simple and professional but with a modern layout that is conveys our new logo and business model

Key aspects of the business:

Property Management
Facility Maintenance
Project Management
Tenant Improvements

Mailing Address:
PO BOX 7816
Riverton CA, 95412

Phone: 209-418-6071
Direct: 209-418-6074

Doyle Marsh
President

Target Market(s)

Commercial property owners

Industry/Entity Type

Real Estate property management

Contact Information for Business Card

Open to all designs but lean toward vertical layouts

Requirements
Must have
• Logo and space to customize name and contact info

```html
<!DOCTYPE html>
<html lang="en">
<head>
<meta charset="UTF-8">
<title>Halven Property Management – Business Card</title>
<link href="https://fonts.googleapis.com/css2?family=Montserrat:wght@400;500;700&display=swap" rel="stylesheet">
<style>
  :root {
    --backdrop: #2b2b2d;
    --ink: #363646;
    --teal: #26a99c;
    --paper: #ffffff;
    --paper-shade: #eeeeee;
    --card-dark: #363747;
    --muted: #4a4a55;
  }
  * { box-sizing: border-box; margin: 0; padding: 0; }
  html, body { width: 1200px; height: 900px; overflow: hidden; }
  body {
    background: var(--backdrop);
    font-family: "Montserrat", sans-serif;
    position: relative;
  }
  .card {
    position: absolute;
    top: 118px;
    width: 380px;
    height: 664px;
    border-radius: 26px;
    overflow: hidden;
  }
  .card--front {
    left: 190px;
    background: linear-gradient(160deg, var(--paper) 40%, var(--paper-shade));
    color: var(--ink);
  }
  .card--back {
    left: 630px;
    background: var(--card-dark);
    color: var(--paper);
  }

  .wordmark {
    position: absolute;
    left: 0; right: 0;
    text-align: center;
    font-weight: 700;
  }
  .wordmark__name {
    display: block;
    font-size: 46px;
    letter-spacing: 6px;
    line-height: 1;
  }
  .wordmark__tag {
    display: block;
    font-size: 12px;
    letter-spacing: 5.5px;
    margin-top: 8px;
  }
  .card--front .wordmark { top: 58px; color: var(--ink); }
  .card--back .wordmark { top: 230px; color: var(--paper); }

  .mark-square {
    position: absolute;
    left: 50%;
    background: var(--teal);
  }
  .card--front .mark-square { top: 160px; width: 120px; height: 120px; margin-left: -60px; }
  .card--back .mark-square { top: 120px; width: 78px; height: 78px; margin-left: -39px; }

  .person {
    position: absolute;
    top: 320px; left: 0; right: 0;
    text-align: center;
  }
  .person__name {
    color: var(--teal);
    font-weight: 700;
    font-size: 30px;
    line-height: 1.1;
  }
  .person__role {
    font-size: 17px;
    font-weight: 500;
    color: var(--muted);
    margin-top: 2px;
  }

  .icon-rule {
    position: absolute;
    top: 398px; left: 30px; right: 30px;
    display: flex;
    align-items: center;
    gap: 6px;
  }
  .icon-rule__line { flex: 1; height: 2px; background: var(--teal); }
  .icon-rule__icon {
    width: 30px; height: 30px;
    border-radius: 6px;
    background: var(--teal);
    display: flex; align-items: center; justify-content: center;
  }

  .contact {
    position: absolute;
    top: 446px; left: 0; right: 0;
    text-align: center;
    font-size: 19px;
    line-height: 1.35;
    color: var(--ink);
  }
  .divider {
    position: absolute;
    top: 560px; left: 50%;
    width: 100px; margin-left: -50px;
    height: 2px; background: var(--teal);
  }
  .mailing {
    position: absolute;
    top: 572px; left: 0; right: 0;
    text-align: center;
    font-size: 18px;
    line-height: 1.3;
    color: var(--ink);
  }

  .services {
    position: absolute;
    top: 420px; left: 0; right: 0;
    list-style: none;
    text-align: center;
    font-size: 18px;
    line-height: 2.1;
  }
  .services li::before {
    content: "";
    display: inline-block;
    width: 6px; height: 6px;
    border-radius: 50%;
    background: var(--teal);
    margin-right: 10px;
    vertical-align: middle;
  }
</style>
</head>
<body>

<section class="card card--front" aria-label="Card front">
  <div class="wordmark">
    <span class="wordmark__name">HALVEN</span>
    <span class="wordmark__tag">PROPERTY MANAGEMENT</span>
  </div>
  <div class="mark-square"></div>

  <div class="person">
    <div class="person__name">Doyle Marsh</div>
    <div class="person__role">President</div>
  </div>

  <div class="icon-rule">
    <span class="icon-rule__line"></span>
    <span class="icon-rule__icon">
      <svg width="16" height="18" viewBox="0 0 16 18"><rect x="4" y="1" width="8" height="16" rx="1.5" fill="none" stroke="#fff" stroke-width="1.6"/><circle cx="8" cy="14" r="1" fill="#fff"/></svg>
    </span>
    <span class="icon-rule__icon">
      <svg width="18" height="16" viewBox="0 0 18 16"><path d="M2 6 Q9 0 16 6 L14 8 L12 6 L6 6 L4 8 Z" fill="#fff"/><rect x="4" y="8" width="10" height="6" rx="1" fill="#fff"/></svg>
    </span>
    <span class="icon-rule__icon">
      <svg width="18" height="14" viewBox="0 0 18 14"><rect x="1" y="1" width="16" height="12" rx="1.5" fill="#fff"/><path d="M1.5 2 L9 8 L16.5 2" fill="none" stroke="#26a99c" stroke-width="1.5"/></svg>
    </span>
    <span class="icon-rule__icon">
      <svg width="18" height="18" viewBox="0 0 18 18"><circle cx="9" cy="9" r="7.5" fill="none" stroke="#fff" stroke-width="1.6"/><ellipse cx="9" cy="9" rx="3.2" ry="7.5" fill="none" stroke="#fff" stroke-width="1.3"/><line x1="1.5" y1="9" x2="16.5" y2="9" stroke="#fff" stroke-width="1.3"/></svg>
    </span>
    <span class="icon-rule__line"></span>
  </div>

  <div class="contact">
    <div>209-418-6074</div>
    <div>209-418-6071</div>
    <div>info@halvenpm.com</div>
    <div>www.halvenpm.com</div>
  </div>
  <div class="divider"></div>
  <div class="mailing">
    <div>Mailing Address:</div>
    <div>PO BOX 7816</div>
    <div>Riverton CA, 95412</div>
  </div>
</section>

<section class="card card--back" aria-label="Card back">
  <div class="mark-square"></div>
  <div class="wordmark">
    <span class="wordmark__name">HALVEN</span>
    <span class="wordmark__tag">PROPERTY MANAGEMENT</span>
  </div>
  <ul class="services">
    <li>Property Management</li>
    <li>Facility Maintenance</li>
    <li>Project Management</li>
    <li>Tenant Improvements</li>
  </ul>
</section>

</body>
</html>
```